Word template Letterhead for Australian Law Firm

We are a small law firm based in Manly, NSW, Australia. We have had a new logo designed for us and wish to freshen up the appearance of our letterhead. We require the letterhead to be in a word document that we can type over. This will not be a ‘printed’ letterhead because we send the majority of our correspondence via email. We would like to see a few options. We have attached our previous letterhead as well as the artwork for our new logo. We like the idea of a watermark across the bottom of the letter but the watermark must stay in place and we must be able to type over it. We are open to some colour throughout the letterhead because the majority of our correspondence is sent electronically. We also use electronic signatures. I have uploaded an example of this.The letterhead must include:-1. Our address details – including our phone number, physical address, website address etc. These details can be found on the copy of our previous letterhead;2. ABN Number;3. The words ‘Corvenda (NSW) Pty Ltd ACN 742 185 903 trading as Shipton & AssociatesLiability limited by a scheme approved under Professional Standards Legislation. The letterhead does not need to include the names and qualifications of the people working at the firm. Thank you.

Target Market(s)

Clients and other parties

Industry/Entity Type

Law Firm

Font styles to use
Other font styles liked:
• raleway, montserrat

Colors

Designer to choose colors to be used in the design.

Requirements
Must have
• Certain wording - please see project description.
• Must be a word document and must be able to type over the watermark etc.
Nice to have
• Watermark at the bottom of the letter.

```html
<!DOCTYPE html>
<html lang="en">
<head>
<meta charset="utf-8">
<title>Ferrow &amp; Associates Letterhead</title>
<link href="https://fonts.googleapis.com/css2?family=Montserrat:wght@400;500;600;700&family=Lato:wght@400;700&display=swap" rel="stylesheet">
<style>
  :root {
    --backdrop: #ececec;
    --paper: #ffffff;
    --navy: #2e3587;
    --indigo: #5a62a0;
    --indigo-light: #7a80b4;
    --gold: #c8b27a;
    --ink: #333333;
    --ink-soft: #444444;
  }
  * { margin: 0; padding: 0; box-sizing: border-box; }
  html, body { width: 998px; height: 1200px; overflow: hidden; background: var(--backdrop); }
  .letterhead {
    position: absolute; left: 91px; top: 20px;
    width: 816px; height: 1160px;
    background: var(--paper);
    box-shadow: 0 0 0 1px #e2e2e2;
    overflow: hidden;
    font-family: 'Lato', sans-serif;
    color: var(--ink);
  }
  .brand-name {
    position: absolute; left: 56px; top: 196px;
    font-family: 'Montserrat', sans-serif; font-weight: 500;
    font-size: 21px; letter-spacing: 1.2px; color: var(--navy);
  }
  .contact-block {
    position: absolute; left: 507px; top: 72px; height: 170px;
    border-left: 2px solid var(--gold);
    padding-left: 17px;
    font-style: normal;
    font-family: 'Montserrat', sans-serif; font-size: 12.5px; line-height: 18.5px;
    color: var(--ink-soft);
  }
  .contact-block .firm { font-weight: 700; color: var(--navy); }
  .contact-list { list-style: none; margin-top: 8px; }
  .contact-list li { display: flex; align-items: center; gap: 9px; }
  .contact-list svg { width: 10px; height: 10px; fill: var(--navy); flex: none; }
  .refs { margin-top: 6px; }
  .ref-label { color: var(--navy); font-weight: 700; }
  .recipient {
    position: absolute; left: 56px; top: 346px;
    font-size: 15px; line-height: 25px; color: var(--ink-soft);
  }
  .recipient .name { font-family: 'Montserrat', sans-serif; font-weight: 600; font-size: 18px; color: var(--navy); }
  .date {
    position: absolute; right: 60px; top: 349px;
    font-family: 'Montserrat', sans-serif; font-size: 15px; color: var(--ink);
  }
  .letter-body {
    position: absolute; left: 56px; top: 480px; width: 700px;
    font-size: 14.4px; line-height: 24.5px; text-align: justify;
  }
  .letter-body p + p { margin-top: 24px; }
  .sign-off {
    position: absolute; left: 56px; top: 760px;
    font-family: 'Montserrat', sans-serif;
  }
  .sign-off .closing { font-size: 17px; color: var(--ink-soft); }
  .sign-off .firm { font-size: 15.5px; font-weight: 600; margin-top: 4px; letter-spacing: .3px; }
  .signatory {
    position: absolute; left: 56px; top: 900px;
    font-family: 'Montserrat', sans-serif;
  }
  .signatory .name { font-size: 16px; font-weight: 600; letter-spacing: .4px; }
  .signatory .email { font-size: 11.5px; margin-top: 5px; color: var(--ink-soft); }
  .footer-band {
    position: absolute; left: 0; bottom: 0; width: 816px; height: 120px;
    background: linear-gradient(90deg, var(--indigo), var(--indigo-light));
  }
  .footer-text {
    position: absolute; left: 0; bottom: 22px; width: 816px; text-align: center;
    font-family: 'Montserrat', sans-serif; font-size: 13.5px; line-height: 20px; color: #ffffff;
  }
  .footer-text .disclaimer { font-style: italic; }
</style>
</head>
<body>
<main class="letterhead">
  <header>
    <div class="brand-name">Ferrow &amp; Associates</div>
    <address class="contact-block">
      <div class="firm">FERROW &amp; ASSOCIATES</div>
      <div>Suite 4, 18 Corella Street</div>
      <div>BRAEMORE NSW 2097</div>
      <ul class="contact-list">
        <li><svg viewBox="0 0 10 10"><path d="M2 0.5l1.8 2.2-1 1.1c.6 1.3 1.5 2.2 2.8 2.8l1.1-1 2.2 1.8-1 1.7C4.7 9.1 0.9 5.3 0.3 1.5z"/></svg>(02) 9481 3720</li>
        <li><svg viewBox="0 0 10 10"><rect x="0.5" y="3" width="9" height="5.5" rx="1"/><rect x="2.5" y="0.5" width="5" height="3"/></svg>(02) 9481 3721</li>
        <li><svg viewBox="0 0 10 10"><path d="M0.5 2h9v6h-9z M1 2.5l4 3 4-3" fill="none" stroke="#2e3587" stroke-width="1"/></svg>reception@corvendalaw.com.au</li>
        <li><svg viewBox="0 0 10 10"><circle cx="5" cy="5" r="4.5"/></svg>www.ferrowassociates.com.au</li>
      </ul>
      <div class="refs"><span class="ref-label">OUR REF:</span> LB:PLN:4821</div>
      <div><span class="ref-label">YOUR REF:</span> Peter Lansing</div>
    </address>
  </header>

  <section class="recipient">
    <div class="name">Daniel Harcourt</div>
    <div>Manager</div>
    <div>1234 Street Name</div>
    <div>Riverton, NC</div>
  </section>
  <div class="date">Date: 09/11/2019</div>

  <article class="letter-body">
    <p>Lorem ipsum dolor sit amet, consectetuer adipiscing elit, sed diam nonummy nibh euismod tincidunt ut laoreet dolore magna aliquam erat volutpat. Ut wisi enim ad minim veniam, quis nostrud exerci tation ullamcorper suscipit lobortis nisl ut aliquip ex ea commodo consequat. Lorem ipsum dolor sit amet, cons ectetuer adipiscing elit, sed diam nonummy nibh euismod tincidunt ut laoreet dolore magna aliquam erat volutpat. Ut wisi enim ad minim veniam, quis nostrud exerci tation ullamcorper suscipit lobortis nisl ut aliquip ex ea commodo consequat. Lorem ipsum dolor sit amet, consectetuer adipiscing elit, sed diam nonummy nibh euismod tincidunt ut laoreet dolore magna aliquam erat volutpat. Ut wisi enim ad minim veniam,</p>
    <p>consequat. Duis autem vel eum iriure dolor in hendrerit in vulputate velit esse molestie consequat, vel illum dolore eu feugiat nulla facilisis at vero eros et accumsan .</p>
  </article>

  <section class="sign-off">
    <div class="closing">Yours faithfully</div>
    <div class="firm">FERROW &amp; ASSOCIATES</div>
  </section>

  <section class="signatory">
    <div class="name">LAURA BRENNAN</div>
    <div class="email">Direct Email: laura@corvendalaw.com.au</div>
  </section>

  <footer>
    <div class="footer-band" role="img" aria-label="Decorative footer band in indigo tones"></div>
    <div class="footer-text">
      <div>Corvenda (NSW) Pty Ltd ACN 742 185 903 trading as Ferrow &amp; Associates</div>
      <div class="disclaimer">Liability limited by a scheme approved under Professional Standards Legislation.</div>
    </div>
  </footer>
</main>
</body>
</html>
```